Bright Path Flyer Design for Virtual Online Clinic. -5.5 x 8.5 inches (half sheet)

We need a clean, modern flyer design for Bright Path, a new virtual walk-in clinic based in British Columbia. The flyer will be used in libraries, pharmacies, and community centers to help residents easily access primary care through their Bright Path NFC access card.
The flyer will ask a question : NEED A DOCTOR? This should be large and attention grabbing.
The design should clearly feature a Bright Path card image (the access card) as the centerpiece and visually show how patients can use it to book appointments. The tone should feel trustworthy, healthcare-oriented, and community-friendly — clean fonts, clear spacing, and strong readability from a distance.

Side One: This card has the NFC Access Card.
NEED A DOCTOR? (Large Font, Attention Grabbing)
How to Book an Appointment using your Bright Path Card
Step 1: Tap Your Card on Your Phone
Hold your card near the back of your phone.
It will activate automatically — no app needed.
The Bright Path scheduler will open.
Step 2: Schedule Your Appointment
Select your clinical concern.
Choose your time window.
Register (only once).
Confirm your appointment.
Step 3: Relax, we’ll take care of the rest
A doctor will call during your scheduled time.
Once booked, you’ll be able to call our office.
No emails, no texts — just a real person.
It’s that simple.
Side Two:
About Bright Path
Created by Dr. Marcus Ferrigan
Bright Path was founded to make healthcare simple and convenient. Prescription renewals. Common infections. Medical notes. And so much more.
Our doctors can address 120+ health concerns virtually — providing quality care without the waiting room. No waiting rooms. Just real doctors providing real care.
Why Patients Choose Bright Path
Easy access – book and be seen from anywhere in BC.
Effortless booking – tap your Bright Path Card to begin.
Trusted physicians – every visit is with a licensed BC family doctor.
How It Works
Book your visit — choose a time window that fits your day.
Join the queue — you’ll be called when it’s your turn.
Speak directly with your doctor — simple, secure, and stress-free.
Convenient Care for Common Concerns

Additional Details.
Please find the domain to be launched soon. I've attached the NFC card file for review, it is 85.5 mm x 54 mm. The card will be glued to the flyer.
I've attached examples of flyers but they are not the look I am seeking and I am looking for creative solutions.
Thank you!
http://brightpath-example.test/

Adult Patients in British Columbia

Healthcare

• Looking for clean lines, uniform appearance, and high legibility i.e poppins

0054AA
0677BA
7BADD7
CADEEF
E8F1F8

• Need A Doctor?
• Elegant style, not too busy, clear layout.
• Clutter, look cheap - review examples.

```html
<!DOCTYPE html>
<html lang="en">
<head>
<meta charset="utf-8">
<title>Bright Path – Half-Sheet Flyer</title>
<link rel="stylesheet" href="https://fonts.googleapis.com/css2?family=Montserrat:wght@400;500;600;700;800&family=Satisfy&display=swap">
<style>
  :root {
    --brand-blue: #3B55A3;
    --brand-blue-soft: #5B72B6;
    --brand-blue-pale: #CADEEF;
    --paper: #F7F7F8;
    --white: #FFFFFF;
    --backdrop: #DCDCDE;
    --sans: "Montserrat", "Poppins", sans-serif;
    --script: "Satisfy", cursive;
  }
  * { box-sizing: border-box; margin: 0; padding: 0; }
  html, body { width: 1200px; height: 802px; overflow: hidden; }
  body { background: var(--backdrop); font-family: var(--sans); color: var(--brand-blue); position: relative; }

  .flyer { position: absolute; top: 31px; width: 478px; height: 740px; background: var(--paper); overflow: hidden; box-shadow: 0 4px 14px rgba(0,0,0,.15); }
  .flyer--front { left: 92px; }
  .flyer--back { left: 630px; background: var(--white); }
  .flyer svg.backdrop { position: absolute; inset: 0; }
  .abs { position: absolute; }

  /* Front */
  .brand-mark { left: 22px; top: 220px; color: var(--white); font-weight: 600; font-size: 15px; display: flex; align-items: center; gap: 6px; }
  .brand-mark .dot { width: 8px; height: 8px; border-radius: 50%; background: var(--white); }
  .access-card { left: 282px; top: 52px; width: 140px; height: 214px; background: var(--white); border: 2px solid var(--brand-blue); overflow: hidden; }
  .access-card .card-name { position: absolute; left: 36px; top: 130px; transform: rotate(-90deg); transform-origin: left top; font-weight: 600; font-size: 17px; white-space: nowrap; }
  .access-card .card-tap { position: absolute; right: 6px; top: 20px; writing-mode: vertical-rl; font-size: 6px; font-weight: 500; }
  .access-card .card-art { position: absolute; left: 0; right: 0; bottom: 0; height: 70px; background: var(--brand-blue); }

  .headline { left: 18px; top: 304px; line-height: .9; font-weight: 800; }
  .headline .small { display: block; font-size: 38px; letter-spacing: 1px; }
  .headline .big { display: block; font-size: 82px; letter-spacing: -1px; }
  .subhead { left: 20px; top: 424px; font-size: 13.5px; font-weight: 600; white-space: nowrap; }

  .steps-icons { left: 0; top: 452px; width: 478px; display: flex; justify-content: space-around; padding: 0 20px; }
  .step-icon { display: flex; flex-direction: column; align-items: center; gap: 4px; }
  .step-icon .label { font-size: 14px; font-weight: 700; }

  .steps-text { left: 14px; top: 578px; width: 450px; display: flex; color: var(--white); }
  .steps-text p { flex: 1; font-size: 10px; font-weight: 500; line-height: 1.3; padding: 0 10px; text-align: center; }
  .steps-text p + p { border-left: 1px solid rgba(255,255,255,.7); }
  .tagline-simple { left: 0; width: 100%; top: 688px; text-align: center; color: var(--white); font-family: var(--script); font-size: 28px; white-space: nowrap; }

  /* Back */
  .about-title { left: 0; width: 100%; top: 26px; text-align: center; font-weight: 800; font-size: 28px; }
  .about-brand { left: 0; width: 100%; top: 60px; text-align: center; font-weight: 600; font-size: 22px; }
  .about-creator { left: 0; width: 100%; top: 96px; text-align: center; font-weight: 700; font-size: 14px; }
  .about-copy { left: 40px; width: 398px; top: 122px; text-align: center; font-size: 9.5px; line-height: 1.45; font-weight: 500; }

  .why-title { left: 22px; top: 300px; font-weight: 800; font-size: 32px; }
  .why-sub { left: 24px; top: 340px; font-weight: 600; font-size: 15px; line-height: 1.15; }
  .benefits { left: 190px; top: 240px; width: 270px; color: var(--white); list-style: none; }
  .benefits li { display: flex; gap: 10px; align-items: center; margin-bottom: 18px; }
  .benefits strong { display: block; font-size: 15px; font-weight: 700; }
  .benefits span { font-size: 9px; }

  .how { left: 0; width: 100%; top: 468px; text-align: center; }
  .how h2 { font-size: 28px; font-weight: 800; margin-bottom: 6px; }
  .how .step strong { display: block; font-size: 14px; font-weight: 700; }
  .how .step span { display: block; font-size: 9px; font-weight: 500; }
  .how .arrow { width: 0; height: 0; margin: 3px auto; border-left: 6px solid transparent; border-right: 6px solid transparent; border-top: 7px solid var(--brand-blue); }
  .tagline-care { left: 0; width: 100%; top: 676px; text-align: center; color: var(--white); font-family: var(--script); font-size: 25px; white-space: nowrap; }
</style>
</head>
<body>

<section class="flyer flyer--front">
  <svg class="backdrop" width="478" height="740" viewBox="0 0 478 740">
    <path d="M0 0 H250 C215 90 230 200 190 292 H0 Z" fill="var(--brand-blue)"/>
    <path d="M0 575 C140 560 330 540 478 520 V740 H0 Z" fill="var(--brand-blue)"/>
    <rect x="262" y="30" width="180" height="262" rx="70" fill="none" stroke="var(--brand-blue)" stroke-width="3"/>
  </svg>
  <div class="abs" role="img" aria-label="Large soaring bird illustration" style="left:110px;top:70px;width:130px;height:170px;background:var(--brand-blue-soft);border-radius:50% 40% 50% 30%;"></div>

  <div class="abs brand-mark"><span class="dot"></span>Bright Path</div>

  <div class="abs access-card">
    <div class="card-name">Bright Path</div>
    <div class="card-tap">Tap Here to Book</div>
    <div class="card-art" role="img" aria-label="Card artwork of bird over mountains"></div>
  </div>

  <h1 class="abs headline"><span class="small">NEED A</span><span class="big">DOCTOR?</span></h1>
  <p class="abs subhead">How to Book an Appointment using your Bright Path Card</p>

  <div class="abs steps-icons">
    <div class="step-icon">
      <svg width="52" height="52" viewBox="0 0 52 52" fill="none" stroke="var(--brand-blue)" stroke-width="2"><rect x="12" y="4" width="26" height="44" rx="4"/><path d="M40 14a8 8 0 0 1 0 12M44 10a14 14 0 0 1 0 20"/></svg>
      <span class="label">Step 1:</span>
    </div>
    <div class="step-icon">
      <svg width="52" height="52" viewBox="0 0 52 52" fill="none" stroke="var(--brand-blue)" stroke-width="2"><rect x="12" y="4" width="26" height="44" rx="4"/><rect x="17" y="14" width="16" height="14"/><path d="M20 21l3 3 6-6"/></svg>
      <span class="label">Step 2:</span>
    </div>
    <div class="step-icon">
      <svg width="52" height="52" viewBox="0 0 52 52" fill="none" stroke="var(--brand-blue)" stroke-width="2"><rect x="12" y="4" width="26" height="44" rx="4"/><path d="M40 8c4 0 6 3 6 6l-3 1-2-3"/></svg>
      <span class="label">Step 3:</span>
    </div>
  </div>

  <div class="abs steps-text">
    <p>Tap Your Card on Your Phone. Hold your card near the back of your phone. It will activate automatically — no app needed. The Bright Path scheduler will open.</p>
    <p>Schedule Your Appointment. Select your clinical concern. Choose your time window. Register (only once).</p>
    <p>Relax, we'll take care of the rest. A doctor will call during your scheduled time. Once booked, you'll be able to call our office. No emails, no texts, just a real person.</p>
  </div>
  <div class="abs tagline-simple">It's that simple.</div>
</section>

<section class="flyer flyer--back">
  <svg class="backdrop" width="478" height="740" viewBox="0 0 478 740">
    <path d="M478 225 H250 C200 225 170 300 170 360 C170 420 200 440 210 450 H478 Z" fill="var(--brand-blue)"/>
    <path d="M0 650 C160 640 330 630 478 610 V740 H0 Z" fill="var(--brand-blue)"/>
  </svg>
  <div class="abs" role="img" aria-label="Bird illustration in flight" style="left:120px;top:260px;width:70px;height:120px;background:var(--brand-blue-soft);border-radius:50% 30% 50% 40%;"></div>

  <h2 class="abs about-title">About</h2>
  <div class="abs about-brand">Bright Path</div>
  <div class="abs about-creator">Created by Dr. Marcus Ferrigan</div>
  <p class="abs about-copy">Bright Path was founded to make healthcare simple and convenient. Prescription renewals. Common infections. Medical notes. And so much more. Our doctors can address 120+ health concerns virtually — providing quality care without the waiting room. No waiting rooms. Just real doctors providing real care.</p>

  <div class="abs why-title">Why</div>
  <div class="abs why-sub">Patients<br>Choose<br>Bright Path</div>

  <ul class="abs benefits">
    <li>
      <svg width="30" height="30" viewBox="0 0 30 30" fill="none" stroke="var(--white)" stroke-width="1.8"><rect x="8" y="2" width="14" height="26" rx="2"/><path d="M15 8a3 3 0 0 1 3 3c0 3-3 6-3 6s-3-3-3-6a3 3 0 0 1 3-3z"/></svg>
      <div><strong>Easy access</strong><span>– book and be seen from anywhere in BC.</span></div>
    </li>
    <li>
      <svg width="30" height="30" viewBox="0 0 30 30" fill="none" stroke="var(--white)" stroke-width="1.8"><rect x="8" y="2" width="14" height="26" rx="2"/><path d="M24 9a5 5 0 0 1 0 8"/></svg>
      <div><strong>Effortless booking</strong><span>– tap your Bright Path Card to begin.</span></div>
    </li>
    <li>
      <svg width="30" height="30" viewBox="0 0 30 30" fill="none" stroke="var(--white)" stroke-width="1.8"><rect x="6" y="16" width="18" height="12" rx="3"/><path d="M11 22l3 3 5-5"/><circle cx="15" cy="9" r="5"/></svg>
      <div><strong>Trusted physicians</strong><span>– every visit is with a licensed BC family doctor.</span></div>
    </li>
  </ul>

  <div class="abs how">
    <h2>How It Works</h2>
    <div class="step"><strong>Book your visit</strong><span>Choose a time window that fits your day.</span></div>
    <div class="arrow"></div>
    <div class="step"><strong>Join the queue</strong><span>You'll be called when it's your turn.</span></div>
    <div class="arrow"></div>
    <div class="step"><strong>Speak directly with your doctor</strong><span>Simple, secure, and stress-free.</span></div>
  </div>

  <div class="abs tagline-care">Convenient Care for Common Concerns</div>
</section>

</body>
</html>
```